Business Card Design Project

We are an incubator company that helps young entrepreneur to launch new ideas into the market. We will be targeting investors or likewise; Angels, young entrepreneurs and technopreneurs.

Our logo is being tasked by artswarm to design, therefore there is no logo for now.
You can us Lanternfield Pte Ltd as the logo for the time being.

Please let us have some versions of modern and yet professional designs; for words, you can indicate e.g (address), (Title)

thanks

Target Market(s)

young entrepreneurs
angels, investors

Industry/Entity Type

Business

Colors
3176b5
ffffff

Requirements
Must have
• able to project out our name; Lanternfield
Should not have
• Nothing childish or cartoon

```html
<!DOCTYPE html>
<html lang="en">
<head>
<meta charset="utf-8">
<title>Lanternfield Business Card</title>
<link href="https://fonts.googleapis.com/css2?family=Questrial&display=swap" rel="stylesheet">
<style>
  :root {
    --brand-blue: #3176b5;
    --brand-blue-deep: #1e4fa8;
    --ink-black: #101113;
    --card-white: #ffffff;
    --backdrop: #d6d3d3;
    --text-light: #f2f2f2;
    --divider: #6b6f75;
  }
  * { margin: 0; padding: 0; box-sizing: border-box; }
  html, body { width: 1200px; height: 900px; overflow: hidden; }
  body {
    background: var(--backdrop);
    font-family: "Questrial", "Helvetica Neue", Arial, sans-serif;
    position: relative;
  }
  .card {
    position: absolute;
    top: 306px;
    width: 504px;
    height: 288px;
    border-radius: 22px;
    overflow: hidden;
    background: var(--card-white);
    box-shadow: 0 10px 24px rgba(0,0,0,0.18);
  }
  .card--front { left: 66px; }
  .card--back { left: 630px; }

  .brand-mark {
    display: block;
    background: var(--brand-blue-deep);
    border-radius: 4px;
  }
  .brand-name {
    color: var(--brand-blue-deep);
    text-transform: uppercase;
    letter-spacing: 1px;
    line-height: 1;
  }

  .front-head {
    height: 160px;
    display: flex;
    flex-direction: column;
    align-items: center;
    justify-content: center;
    gap: 14px;
    padding-top: 10px;
  }
  .front-head .brand-mark { width: 46px; height: 46px; }
  .front-head .brand-name { font-size: 30px; }
  .tagline-band {
    height: 14px;
    background: var(--brand-blue);
    color: var(--card-white);
    font-size: 10px;
    letter-spacing: 9px;
    text-transform: uppercase;
    line-height: 14px;
    text-align: center;
    white-space: nowrap;
  }
  .front-body {
    height: 114px;
    background: var(--ink-black);
    display: flex;
    padding: 14px 0 0 0;
  }
  .person {
    width: 186px;
    text-align: right;
    padding-right: 16px;
    border-right: 1px solid var(--divider);
    height: 80px;
  }
  .person__name { color: var(--brand-blue); font-size: 18px; }
  .person__title { color: var(--text-light); font-size: 13px; margin-top: 3px; }
  .contact-list {
    list-style: none;
    padding-left: 14px;
    color: var(--text-light);
    font-size: 17px;
  }
  .contact-list li {
    display: flex;
    align-items: center;
    gap: 6px;
    height: 22px;
  }
  .contact-list svg { width: 17px; height: 17px; flex: none; }

  .card--back {
    display: flex;
    flex-direction: column;
    align-items: center;
    justify-content: center;
  }
  .card--back .brand-mark { width: 96px; height: 96px; border-radius: 8px; margin-bottom: 34px; }
  .card--back .brand-name { font-size: 40px; }
  .back-tagline {
    color: var(--ink-black);
    font-size: 11px;
    letter-spacing: 3px;
    text-transform: uppercase;
    margin-top: 4px;
    padding-left: 60px;
    white-space: nowrap;
  }
</style>
</head>
<body>

<section class="card card--front" aria-label="Business card front">
  <header class="front-head">
    <span class="brand-mark" aria-hidden="true"></span>
    <span class="brand-name">Lanternfield</span>
  </header>
  <div class="tagline-band">Lighting Ideas Into Markets</div>
  <div class="front-body">
    <div class="person">
      <p class="person__name">Marcus Hale</p>
      <p class="person__title">Manager</p>
    </div>
    <ul class="contact-list">
      <li>
        <svg viewBox="0 0 24 24" aria-hidden="true"><path fill="#3176b5" d="M6.6 10.8a15 15 0 0 0 6.6 6.6l2.2-2.2c.3-.3.7-.4 1-.2 1.1.4 2.300.6 3.6.6.6 0 1 .4 1 1V20c0 .6-.4 1-1 1A17 17 0 0 1 3 4c0-.6.4-1 1-1h3.5c.6 0 1 .4 1 1 0 1.3.2 2.5.6 3.6.1.3 0 .7-.2 1z"/></svg>
        919 555 0142
      </li>
      <li>
        <svg viewBox="0 0 24 24" aria-hidden="true"><g fill="none" stroke="#3176b5" stroke-width="2"><circle cx="12" cy="12" r="9"/><ellipse cx="12" cy="12" rx="4" ry="9"/><line x1="3" y1="12" x2="21" y2="12"/></g></svg>
        www.lanternfield.com
      </li>
      <li>
        <svg viewBox="0 0 24 24" aria-hidden="true"><rect x="3" y="6" width="18" height="13" rx="1" fill="#3176b5"/><path d="M3 7l9 6 9-6" fill="none" stroke="#101113" stroke-width="1.6"/></svg>
        hello@lanternfield.com
      </li>
      <li>
        <svg viewBox="0 0 24 24" aria-hidden="true"><path fill="#3176b5" d="M12 3l10 9h-3v9h-5v-6h-4v6H5v-9H2z"/></svg>
        Elm Harbor, Carolina
      </li>
    </ul>
  </div>
</section>

<section class="card card--back" aria-label="Business card back">
  <span class="brand-mark" aria-hidden="true"></span>
  <span class="brand-name">Lanternfield</span>
  <p class="back-tagline">Lighting Ideas Into Markets</p>
</section>

</body>
</html>
```